Visitenkarte und Briefpapier für Rechtsanwaltskanzlei
Zielgruppe
Neugründung einer Rechtsanwaltskanzlei für Strafrecht mit einem Anwalt
Aufgabenstellung
Ich möchte gerne Briefpapier und Visitenkarten mit einem schlichten aber professionellen Charakter für meine neue Rechtsanwaltskanzlei erstellen lassen. Die Erscheinung soll modern, sachlich und klar sein. Es soll kein Logo verwendet werden, sondern nur der Namensschriftzug "Dr. Harald Obst", gerne in Großbuchstaben. Siehe dazu beispielhaft die Design-Charakter der angegeben Links.
Die Visitenkarte sollen als druckfähiges PDF und das Briefpapier zusätzlich als Word-Dokument geliefert werden.

```html
<!DOCTYPE html>
<html lang="de">
<head>
<meta charset="utf-8">
<title>Dr. Harald Obst – Visitenkarte und Briefpapier</title>
<link rel="stylesheet" href="https://fonts.googleapis.com/css2?family=Raleway:wght@600&family=Josefin+Sans:wght@400&family=Josefin+Slab:wght@400&display=swap">
<style>
  :root {
    --paper: #ffffff;
    --ink: #1d1d1d;
    --ink-soft: #444444;
    --ink-muted: #8a8a8a;
    --body-text: #555555;
    --stage: #d4d4d4;
    --frame: #8c8c8c;
  }
  * { margin: 0; padding: 0; box-sizing: border-box; }
  html, body { width: 1200px; height: 2399px; overflow: hidden; background: var(--paper); }
  body { position: relative; font-family: "Josefin Sans", sans-serif; color: var(--ink); }

  .wordmark {
    font-family: "Raleway", sans-serif;
    font-weight: 600;
    text-transform: uppercase;
    letter-spacing: 0.04em;
    white-space: nowrap;
  }
  .wordmark .gap { display: inline-block; width: 0.3em; }

  .hero-title {
    position: absolute; top: 202px; left: 0; width: 1200px;
    text-align: center; font-size: 50px; color: var(--ink);
  }

  .stage { position: absolute; left: 0; width: 1200px; background: var(--stage); }
  .stage--cards { top: 817px; height: 482px; }
  .stage--letter { top: 1352px; height: 893px; }

  .card {
    position: absolute; width: 487px; height: 306px;
    background: var(--paper);
  }
  .card--outlined { border: 1px solid var(--frame); }
  .card__name {
    position: absolute; top: 104px; left: 0; width: 100%;
    text-align: center; font-size: 26px;
  }
  .card__tagline {
    position: absolute; top: 251px; left: 0; width: 100%;
    text-align: center; font-size: 13px; letter-spacing: 0.03em;
    text-transform: uppercase; color: var(--ink);
  }
  .card__contact {
    position: absolute; top: 160px; left: 0; width: 100%;
    text-align: center; font-size: 13.5px; line-height: 22px; color: var(--ink);
  }
  .card--print .card__name { color: var(--ink-soft); }

  .letterhead {
    position: absolute; left: 275px; top: 97px; width: 486px; height: 684px;
    background: var(--paper);
  }
  .letterhead__name {
    position: absolute; top: 72px; left: 0; width: 100%;
    text-align: center; font-size: 14px; color: var(--ink-muted);
  }
  .letterhead__body {
    position: absolute; top: 211px; left: 67px; width: 351px;
    font-family: "Josefin Slab", serif; font-size: 8.6px; line-height: 8.25px;
    color: var(--body-text); text-align: justify; hyphens: auto;
  }
  .letterhead__body p { margin-bottom: 12px; }

  .card--mini {
    position: absolute; left: 825px; top: 151px; width: 197px; height: 127px;
    background: var(--paper);
  }
  .card--mini .card__name { top: 38px; font-size: 11px; color: var(--ink); }
  .card--mini .card__tagline { top: 93px; font-size: 5px; }
</style>
</head>
<body>

  <h1 class="hero-title wordmark">Dr.<span class="gap"></span>Harald Obst</h1>

  <section class="card card--outlined" style="left:84px; top:458px;" aria-label="Visitenkarte Vorderseite">
    <div class="card__name wordmark">Dr.<span class="gap"></span>Harald Obst</div>
    <div class="card__tagline">Rechtsanwaltskanzlei für Strafrecht</div>
  </section>
  <section class="card card--outlined" style="left:621px; top:457px;" aria-label="Visitenkarte Rückseite">
    <address class="card__contact" style="font-style:normal;">
      Erlenweg 7<br>
      85371 Lindaufeld<br>
      telefon: 08163 – 52 31 48<br>
      telefax: 08163 – 52 31 49<br>
      e-mail: dr.obst@mailvora.de
    </address>
  </section>

  <div class="stage stage--cards">
    <section class="card card--print" style="left:84px; top:88px;" aria-label="Visitenkarte Vorderseite, Druckansicht">
      <div class="card__name wordmark">Dr.<span class="gap"></span>Harald Obst</div>
      <div class="card__tagline">Rechtsanwaltskanzlei für Strafrecht</div>
    </section>
    <section class="card card--print" style="left:621px; top:88px;" aria-label="Visitenkarte Rückseite, Druckansicht">
      <address class="card__contact" style="font-style:normal;">
        Erlenweg 7<br>
        85371 Lindaufeld<br>
        telefon: 08163 – 52 31 48<br>
        telefax: 08163 – 52 31 49<br>
        e-mail: dr.obst@mailvora.de
      </address>
    </section>
  </div>

  <div class="stage stage--letter">
    <article class="letterhead" aria-label="Briefpapier">
      <div class="letterhead__name wordmark">Dr.<span class="gap"></span>Harald Obst</div>
      <div class="letterhead__body">
        <p>Lorem ipsum dolor sit amet,</p>
        <p>Lorem ipsum dolor sit amet, consectetur adipiscing elit. Donec orci purus, luctus vitae dignissim eu, iaculis sed purus. Vivamus faucibus, ipsum nec aliquet viverra, leo mauris condimentum ligula, sit amet sagittis enim ligula quis arcu. Nam egestas tortor id nisi porttitor mattis. In tortor ante, ultricies in suscipit a, tempus non massa. Vivamus et auctor mi. Fusce vel massa nulla. Phasellus nec eros mauris, et scelerisque orci. Donec malesuada orci vitae nulla accumsan porta a id massa. Quisque accumsan iaculis magna sit amet fringilla. Maecenas consequat, magna eget tincidunt semper, odio nibh rutrum mi, id feugiat ante nisi eu risus. Vestibulum nunc orci, rhoncus a placerat in, ultricies in mi. Cras mattis varius eros, vel fringilla nisi suscipit eget.</p>
        <p>Quisque scelerisque sagittis nulla at porttitor. Mauris a justo et tellus interdum tristique. Sed id augue vitae urna euismod commodo aliquet a quam. Pellentesque arcu velit, cursus et malesuada ut, consequat et diam. Nullam erat sem, rhoncus id ullamcorper vitae, rhoncus et arcu. In ultricies ultricies nulla, ut rutrum nisi iaculis at. Donec eu magna a metus ornare faucibus. Fusce aliquet faucibus ultricies. Morbi semper, est id tincidunt gravida, sem arcu adipiscing lacus, ac bibendum nulla leo eu purus. Quisque nec diam sed risus consectetur a ccumsan quis quis nibh. Vestibulum id purus lorem.</p>
        <p>Vivamus vehicula accumsan lacinia. Aliquam erat volutpat. Pellentesque consequat venenatis velit non gravida. Etiam et sem et nulla congue aliquam sed eget augue. Nulla facilisi. Pellentesque habitant morbi tristique senectus et netus et malesuada fames ac turpis egestas. Nulla a elit at sem iaculis congue. Nullam mollis tristique lobortis.</p>
      </div>
    </article>

    <section class="card card--mini" aria-label="Visitenkarte, klein">
      <div class="card__name wordmark">Dr.<span class="gap"></span>Harald Obst</div>
      <div class="card__tagline">Rechtsanwaltskanzlei für Strafrecht</div>
    </section>
  </div>

</body>
</html>
```